Website for B2B SaaS Financial Segmentation Service

I need a website that explains a service I provide called Kestrel-Fold Analysis and gives visitors a professional-looking opt-in form for my Keap CRM. I also want it to have a CMS that I can easily edit when I want to update images and copy.

Kestrel-Fold Analysis is a dashboard I produce that gives B2B SaaS executives an economic segmentation of their active revenue build. It breaks the revenue build into 3 categories and illustrates how much of the revenue build is in each category.

The red category is customers who have not repaid what I call "Poor Man's" cost of revenue and are therefore unprofitable.

The green category is customers who have repaid Poor Man's cost of revenue and are therefore profitable.

The blue category is customers who have repaid Poor Man's cost of revenue, but are deceptively unprofitable for the business because of how much servicing them costs.

I call the green category the "Harbor of Tallow."

The website will contain descriptions of the overall concept and each of the categories and have lots of calls to action that get them to engage with me through the opt-in form.

I might also be interested in a live chat feature for the site, but not if that is an expensive monthly option.

Target Market(s)

B2B SaaS companies

Industry/Entity Type

B2B SaaS

Coding

Coded - Design and coding required

Number of Pages Required

3 page

Requirements
Must have
• A strong landing page with a good drill-down page I can reuse and a blog I can post to. Color schema that matches the logo I uploaded.

```html
<!DOCTYPE html>
<html lang="en">
<head>
<meta charset="utf-8">
<title>Kestrel-Fold Analysis</title>
<link rel="stylesheet" href="https://fonts.googleapis.com/css2?family=Poppins:wght@500;600;700;800&family=Montserrat:wght@400;500&family=Arimo:wght@400&display=swap">
<style>
:root{
  --blue:#3f87f5;
  --blue-btn:#4b91f6;
  --green:#15dcc0;
  --red:#ef2125;
  --ink:#111;
  --muted-bg:#f4f4f4;
  --footer:#121212;
  --field:#fafafa;
  --ribbon-soft:linear-gradient(180deg,rgba(63,135,245,.28) 0%,rgba(21,220,192,.28) 50%,rgba(239,33,37,.28) 100%);
}
*{box-sizing:border-box;margin:0;padding:0}
html,body{width:1200px;height:3404px;overflow:hidden;background:#fff}
body{position:relative;font-family:"Montserrat",sans-serif;color:var(--ink)}
.abs{position:absolute}
.btn{position:absolute;display:flex;align-items:center;justify-content:center;color:#fff;font-family:"Poppins",sans-serif;font-weight:700;border-radius:2px;text-transform:uppercase;text-decoration:none}

/* hero */
.hero{position:absolute;left:0;top:0;width:1200px;height:638px;background:linear-gradient(90deg,#5d6165 0%,#8a8d90 30%,#c9cbcd 48%,#ecedee 62%,#f3f3f3 100%)}
.ribbon{position:absolute;background:var(--ribbon-soft);border-radius:6px}
.brand{position:absolute;display:flex;align-items:center;gap:10px;font-family:"Poppins",sans-serif;font-weight:600;color:#fff;letter-spacing:5px;font-size:13px;line-height:1.5}
.brand .mark{width:14px;height:14px;background:#fff}
.nav{position:absolute;top:54px;font-family:"Arimo",sans-serif;font-size:14px;color:#111}
.hero-title{position:absolute;left:460px;top:372px;font-family:"Poppins",sans-serif;font-weight:800;font-size:58px;line-height:88px;letter-spacing:12px;color:#000}

/* about */
.h2{position:absolute;font-family:"Poppins",sans-serif;font-weight:700;color:#000}
.about-p{position:absolute;left:109px;width:566px;font-size:15.3px;line-height:32px;color:#111}
.photo{position:absolute}

/* categories */
.cats{position:absolute;left:0;top:1237px;width:1200px;height:1168px;background:var(--muted-bg)}
.cat-title{position:absolute;font-family:"Poppins",sans-serif;font-weight:700;font-size:21px}
.cat-text{position:absolute;font-size:11.5px;line-height:24px;width:400px}
.small-btn{font-size:11px;height:40px;width:123px}

/* contact */
.field{position:absolute;background:var(--field);box-shadow:0 2px 6px rgba(0,0,0,.06);font-size:15px;color:#333;padding-left:19px;display:flex;align-items:center}
.field.tall{align-items:flex-start;padding-top:17px}

/* footer */
.footer{position:absolute;left:0;top:2995px;width:1200px;height:409px;background:var(--footer);color:#fff}
.f-head{position:absolute;font-family:"Poppins",sans-serif;font-weight:700;font-size:18px;text-transform:uppercase;transform:translateX(-50%);white-space:nowrap}
.f-link{position:absolute;font-family:"Arimo",sans-serif;font-size:15px;transform:translateX(-50%);white-space:nowrap}
.social{position:absolute;width:30px;height:30px;border-radius:50%;background:#fff;display:flex;align-items:center;justify-content:center}
</style>
</head>
<body>

<!-- HERO -->
<section class="hero" role="img" aria-label="Photo of a person reviewing an analytics dashboard on a laptop"></section>
<div class="ribbon" style="left:62px;top:20px;width:654px;height:641px" role="img" aria-label="Stepped blue, green and red ribbon illustration running down the hero"></div>
<div class="brand" style="left:116px;top:70px"><span class="mark"></span><span>KESTREL-FOLD<br>ANALYSIS</span></div>
<nav>
  <span class="nav" style="left:619px">Home</span>
  <span class="nav" style="left:710px">About Us</span>
  <span class="nav" style="left:822px">Services</span>
  <span class="nav" style="left:931px">Blog</span>
  <span class="nav" style="left:1013px">Contact us</span>
</nav>
<h1 class="hero-title">KESTREL-FOLD<br>ANALYSIS</h1>
<a class="btn" style="left:460px;top:554px;width:156px;height:53px;background:var(--blue-btn);font-size:15px">Get Started</a>

<!-- ABOUT -->
<h2 class="h2" style="left:112px;top:760px;font-size:32px">ABOUT US&nbsp; KESTREL-FOLD ANALYSIS</h2>
<p class="about-p" style="top:822px">Lorem ipsum dolor sit amet, consectetur adipiscing elit, sed do eiusmod tempor incididunt ut labore et dolore magna aliqua. Quis ipsum suspendisse ultrices gravida. Risus commodo viverra maecenas accumsan lacus vel facilisis.</p>
<p class="about-p" style="top:981px">Lorem ipsum dolor sit amet, consectetur adipiscing elit, sed do eiusmod tempor incididunt ut labore et dolore magna aliqua. Quis ipsum suspendisse ultrices gravida.</p>
<a class="btn" style="left:110px;top:1097px;width:161px;height:53px;background:var(--blue-btn);font-size:15px">Learn More</a>
<svg class="abs" style="left:0;top:0" width="1200" height="1200" viewBox="0 0 1200 1200">
  <path d="M777 851 V788 H866" stroke="var(--red)" stroke-width="2" fill="none"/>
  <path d="M1051 978 V1068 H977" stroke="var(--red)" stroke-width="2" fill="none"/>
</svg>
<div class="photo" style="left:866px;top:753px;width:220px;height:225px;background:linear-gradient(135deg,#cfd3d6,#8f9599 60%,#e4e6e8)" role="img" aria-label="Photo of a smiling support agent wearing a headset"></div>
<div class="photo" style="left:699px;top:851px;width:278px;height:284px;background:linear-gradient(135deg,#1c2a3d,#2d4663 50%,#3f5f7e)" role="img" aria-label="Photo of a laptop with glowing data charts"></div>

<!-- CATEGORIES -->
<section class="cats"></section>
<h2 class="h2" style="left:0;width:1200px;text-align:center;top:1326px;font-size:33px">OUR CATEGORIES</h2>
<div class="ribbon" style="left:124px;top:1454px;width:656px;height:647px" role="img" aria-label="Stepped blue, green and red ribbon illustration linking the three categories"></div>
<svg class="abs" style="left:0;top:1400px" width="1200" height="820" viewBox="0 1400 1200 820">
  <line x1="644" y1="1530" x2="724" y2="1530" stroke="var(--blue)" stroke-width="2"/>
  <circle cx="644" cy="1530" r="9" fill="var(--blue)"/>
  <line x1="467" y1="1863" x2="605" y2="1863" stroke="var(--green)" stroke-width="2"/>
  <circle cx="605" cy="1863" r="9" fill="var(--green)"/>
  <line x1="200" y1="2101" x2="200" y2="2200" stroke="var(--red)" stroke-width="2"/>
  <circle cx="200" cy="2200" r="10" fill="var(--red)"/>
</svg>

<h3 class="cat-title" style="left:163px;top:1477px">BLUE CATEGORY</h3>
<p class="cat-text" style="left:163px;top:1514px;width:395px">customers who have repaid Poor Man's cost of revenue, but are deceptively unprofitable for the business because of how much servicing them costs.</p>
<a class="btn small-btn" style="left:164px;top:1603px;background:var(--blue-btn)">Learn More</a>

<h3 class="cat-title" style="left:652px;top:1846px">GREEN CATEGORY</h3>
<p class="cat-text" style="left:652px;top:1882px;width:385px">customers who have repaid Poor Man's cost of revenue and are therefore profitable. I call the green category the "Harbor of Tallow."</p>
<a class="btn small-btn" style="left:653px;top:1969px;background:var(--green)">Learn More</a>

<h3 class="cat-title" style="left:239px;top:2190px">RED CATEGORY</h3>
<p class="cat-text" style="left:236px;top:2227px;width:385px">customers who have not repaid what I call "Poor Man's" cost of revenue and are therefore unprofitable.</p>
<a class="btn small-btn" style="left:238px;top:2285px;background:var(--red)">Learn More</a>

<!-- CONTACT -->
<h2 class="h2" style="left:0;width:1200px;text-align:center;top:2494px;font-size:33px">CONTACT US</h2>
<form>
  <div class="field" style="left:192px;top:2584px;width:386px;height:50px">First Name</div>
  <div class="field" style="left:593px;top:2584px;width:386px;height:50px">Last Name</div>
  <div class="field" style="left:192px;top:2650px;width:386px;height:50px">Email</div>
  <div class="field" style="left:593px;top:2650px;width:386px;height:50px">Phone</div>
  <div class="field tall" style="left:192px;top:2718px;width:788px;height:105px">How Can We Help?</div>
  <a class="btn" style="left:489px;top:2852px;width:194px;height:53px;background:var(--blue-btn);font-size:15px">Submit</a>
</form>

<!-- FOOTER -->
<footer class="footer">
  <div class="brand" style="left:110px;top:115px;font-size:15px;letter-spacing:6px"><span class="mark"></span><span>KESTREL-FOLD<br>ANALYSIS</span></div>
  <div class="social" style="left:183px;top:186px"><span style="width:10px;height:10px;border-radius:50%;background:var(--green)"></span></div>
  <div class="social" style="left:220px;top:186px"><span style="width:10px;height:10px;border-radius:50%;background:var(--green)"></span></div>
  <div class="social" style="left:257px;top:186px"><span style="width:10px;height:10px;border-radius:50%;background:var(--green)"></span></div>

  <div class="f-head" style="left:562px;top:62px">Subscribe to our newsletter</div>
  <p style="position:absolute;left:397px;top:110px;width:330px;text-align:center;font-family:'Arimo',sans-serif;font-size:15px;line-height:25px">Lorem ipsum dolor sit amet, consectetur adipiscing elit, sed do</p>
  <div style="position:absolute;left:419px;top:178px;width:272px;height:40px;border-radius:20px;background:#fff;display:flex;align-items:center;padding-left:22px;color:#999;font-size:14px">Enter Your Email</div>
  <svg class="abs" style="left:651px;top:180px" width="36" height="36" viewBox="0 0 36 36">
    <circle cx="18" cy="18" r="18" fill="var(--green)"/>
    <path d="M10 18 L26 11 L21 26 L18 20 Z" fill="#fff"/>
  </svg>

  <div class="f-head" style="left:841px;top:65px">Support</div>
  <span class="f-link" style="left:841px;top:111px">Terms &amp; Conditions</span>
  <span class="f-link" style="left:838px;top:141px">Privacy Policy</span>
  <span class="f-link" style="left:840px;top:172px">About Us</span>
  <span class="f-link" style="left:840px;top:202px">Support</span>

  <div class="f-head" style="left:1019px;top:65px">Quick Link</div>
  <span class="f-link" style="left:1021px;top:110px">Home</span>
  <span class="f-link" style="left:1021px;top:140px">About Us</span>
  <span class="f-link" style="left:1021px;top:170px">Services</span>
  <span class="f-link" style="left:1021px;top:200px">Blog</span>
  <span class="f-link" style="left:1021px;top:230px">Contact us</span>

  <div style="position:absolute;left:103px;top:305px;width:975px;height:1px;background:#2e2e2e"></div>
  <p style="position:absolute;left:0;width:1200px;text-align:center;top:340px;font-family:'Arimo',sans-serif;font-size:15px">©Copyrights 2023&nbsp; Kestrel-Fold Analysis &nbsp;|&nbsp;&nbsp; All Rights Reserved</p>
</footer>

<!-- chat bubble -->
<svg class="abs" style="left:1119px;top:2968px" width="52" height="50" viewBox="0 0 52 50">
  <circle cx="24" cy="26" r="23" fill="var(--green)"/>
  <path d="M14 20 h16 a3 3 0 0 1 3 3 v6 a3 3 0 0 1 -3 3 h-9 l-5 4 v-4 h-2 a3 3 0 0 1 -3 -3 v-6 a3 3 0 0 1 3 -3z" fill="#fff"/>
  <circle cx="44" cy="8" r="7" fill="var(--red)"/>
  <text x="44" y="11.5" font-family="Arimo,sans-serif" font-size="10" fill="#fff" text-anchor="middle">1</text>
</svg>

</body>
</html>
```